Redesign der Systemmails von motivhafen.de
Zielgruppe
Wir sind die Macher von motivhafen.de und wollen unsere Standardmails, die systemseitig verschickt werden, schöner und wertiger gestalten.
Aufgabenstellung
Wir sind der Meinung, dass unsere System-E-Mails ein Redesign nötig haben. Daher würden wir Dich bitten, uns Deinen Input zu geben. Die Mails sollen schlichter und moderner gestaltet werden. Folgende Elemente bedürfen aus unserer Sicht der Überarbeitung:
Schrift -> Aktuell verwenden wir Lucida Sans Unicode als Schrift für die Mails. Die Schrift passt aber nicht mehr so gut zur Seite. Auf der Seite verwenden wir inzwischen die Lato (leider keine Systemschrift).
Bitte schlage eine aus Deiner Sicht geeignete Systemschrift vor.
Buttonstyle -> Bitte einen frischen Buttonstyle vorschlagen
Schriftgröße und Farbe der Headline, des Fließtextes und des Footers -> Bitte harmonische Einteilung finden
Einen Screenshot einer aktuellen Mail ist anbei, außerdem einige Beispiele gelungener Mails anderer Unternehmen.
Die Datenlieferung sollte dann bitte als PSD und einer textlichen Beschreibung der Schriften, Schriftgrößen und Farbwerte erfolgen.
Bitte folgenden Text für die Gestaltung verwenden:
Hallo VORNAME NACHNAME,
Ihr Projekt 'BEISPIELPROJEKTTITEL' ist abgelaufen. Als nächstes sollten Sie ein Gewinner-Design bestimmen:
Button [Gewinner bestimmen]
Sie möchten noch Feinheiten am Design ändern lassen? Kein Problem: Finale Änderungen am Gewinnerdesign erledigt der Designer gerne im Rahmen der Datenübergabe. Küren Sie einfach Ihren Favoriten zum Gewinner und teilen Sie dem Designer Ihre Änderungswünsche in der Datenübergabe mit. Erst wenn Sie bestätigt haben, dass alle Daten mit den gewünschten Überarbeitungen vollständig übergeben wurden, wird das Preisgeld an den Designer transferiert.
Sie können sich zwischen Ihren Favoriten nicht entscheiden?
Kein Problem, nutzen Sie einfach unser praktisches Design-Voting und lassen Sie Familie, Freunde, Bekannte und Kollegen abstimmen. So sehen Sie, welches Design am besten ank..

```html
<!DOCTYPE html>
<html lang="de">
<head>
<meta charset="utf-8">
<title>motivhafen.de – Projekt abgelaufen</title>
<link rel="stylesheet" href="https://fonts.googleapis.com/css2?family=Arimo:wght@400;700&display=swap">
<style>
  :root {
    --page-bg: #f1f1f1;
    --card-bg: #ffffff;
    --card-border: #e2e2e2;
    --text: #3a3a3a;
    --text-soft: #555555;
    --accent: #4ab3d6;
    --button: #45d35a;
    --button-text: #ffffff;
    --link: #2b54c9;
    --divider: #e6e6e6;
    --logo: #4a4a4a;
  }
  * { box-sizing: border-box; margin: 0; padding: 0; }
  html, body {
    width: 710px; height: 1200px; overflow: hidden;
    background: var(--page-bg);
    font-family: "Arimo", Helvetica, Arial, sans-serif;
    color: var(--text);
  }
  .mail { width: 710px; height: 1200px; position: relative; }

  .brand {
    height: 130px;
    display: flex; align-items: center; justify-content: center; gap: 12px;
    padding-top: 4px;
  }
  .brand-mark { width: 26px; height: 26px; background: var(--accent); }
  .brand-name { font-size: 36px; font-weight: 400; color: var(--logo); letter-spacing: -0.3px; }

  .card {
    margin: 0 auto; width: 606px; height: 888px;
    background: var(--card-bg);
    border: 1px solid var(--card-border);
    padding: 42px 37px 0;
  }
  .greeting { text-align: center; font-size: 26px; font-weight: 400; color: var(--text); }
  .greeting .recipient { color: var(--accent); font-weight: 700; }
  .intro {
    margin: 22px auto 0; width: 420px; text-align: center;
    font-size: 20px; line-height: 26px; color: var(--text);
  }
  .cta {
    display: flex; align-items: center; justify-content: center;
    margin: 36px auto 0; width: 384px; height: 73px;
    background: var(--button); border-radius: 5px;
    color: var(--button-text); font-size: 21px; font-weight: 700;
    text-decoration: none; letter-spacing: 0.2px;
  }
  .divider { border: 0; border-top: 1px solid var(--divider); margin: 38px 0 0; }

  .section { margin-top: 32px; }
  .section + .section { margin-top: 22px; }
  .section-title { font-size: 19px; line-height: 26px; font-weight: 700; color: var(--accent); }
  .section p, .contact {
    margin-top: 9px; font-size: 16.5px; line-height: 28px; color: var(--text);
  }
  .section a, .contact a { color: var(--link); text-decoration: none; border-bottom: 1px solid var(--link); }
  .contact { margin-top: 26px; }
  .phone { display: block; margin-top: 6px; }

  .legal {
    width: 606px; margin: 38px auto 0; padding: 0 37px;
    font-size: 11px; line-height: 22px; color: var(--text-soft);
  }
  .legal-title { font-weight: 700; color: var(--text); }
  .legal a { color: var(--link); text-decoration: none; border-bottom: 1px solid var(--link); }
  .legal .plain-link { color: var(--text-soft); border-bottom-color: var(--text-soft); }
</style>
</head>
<body>
<div class="mail">
  <header class="brand">
    <span class="brand-mark" aria-hidden="true"></span>
    <span class="brand-name">motivhafen.de</span>
  </header>

  <main class="card">
    <h1 class="greeting">Hallo <span class="recipient">VORNAME NACHNAME</span>,</h1>
    <p class="intro">Ihr Projekt 'BEISPIELPROJEKTTITEL' ist abgelaufen. Als nächstes sollten Sie ein Gewinner-Design bestimmen:</p>
    <a class="cta" href="#">GEWINNER BESTIMMEN</a>
    <hr class="divider">

    <section class="section">
      <h2 class="section-title">Sie möchten noch Feinheiten am Design ändern lassen?</h2>
      <p>Kein Problem: Finale Änderungen am Gewinnerdesign erledigt der Designer gerne im Rahmen der Datenübergabe. Küren Sie einfach Ihren Favoriten zum Gewinner und teilen Sie dem Designer Ihre Änderungswünsche in der Datenübergabe mit. Erst wenn Sie bestätigt haben, dass alle Daten mit den gewünschten Überarbeitungen vollständig übergeben wurden, wird das Preisgeld an den Designer transferiert.</p>
    </section>

    <section class="section">
      <h2 class="section-title">Sie können sich zwischen Ihren Favoriten nicht entscheiden?</h2>
      <p>Kein Problem, nutzen Sie einfach unser praktisches <a href="#">Design-Voting</a> und lassen Sie Familie, Freunde, Bekannte und Kollegen abstimmen. So sehen Sie, welches Design am besten ankommt.</p>
    </section>

    <p class="contact">Sollten Sie noch Fragen haben, schreiben Sie uns einfach eine Mail unter <a href="#">support@motivhafen.de</a> oder rufen Sie uns an: <span class="phone">0431-55872140</span></p>
  </main>

  <footer class="legal">
    <p class="legal-title">Impressum</p>
    <p><a href="#">motivhafen.de</a> GmbH, Hafenstraße 8, 24103 Kiel, Deutschland, +49 (0)431-55872140</p>
    <p>Geschäftsführer: Jonas Brandt und Lena Wiechert, Amtsgericht Kiel: HRB 31572</p>
    <p>Sie können Ihre Maileinstellungen jederzeit ändern, indem Sie hier klicken:</p>
    <p><a class="plain-link" href="#">https://www.motivhafen.de/konto/einstellungen</a>.</p>
  </footer>
</div>
</body>
</html>
```